Ledgerwise Business Card Design

Business Card Design for new business called Ledgerwise focused on selling business software to small and medium size companies who have outgrown Tallymark. Similar companies would be Tallymark, Nuvo, CoreFlow. Also Dealharbor would be good to look at for additional ideas around look and feel.

Target Market(s)

Business to Business

Industry/Entity Type

Information Technology

Contact Information for Business Card

Standard Business Card Information

Font styles to use
Sans Serif

```html
<!DOCTYPE html>
<html lang="en">
<head>
<meta charset="utf-8">
<title>Ledgerwise Business Card</title>
<link rel="stylesheet" href="https://fonts.googleapis.com/css2?family=Roboto:wght@400;500&display=swap">
<style>
  :root {
    --navy: #0f5286;
    --orange: #f38421;
    --paper: #ebecee;
    --white: #ffffff;
    --canvas: #ffffff;
  }
  * { margin: 0; padding: 0; box-sizing: border-box; }
  html, body {
    width: 1200px; height: 1200px; overflow: hidden;
    background: var(--canvas);
    font-family: "Roboto", Arial, sans-serif;
  }
  .sheet { position: relative; width: 1200px; height: 1200px; }
  .card { position: absolute; top: 70px; width: 536px; height: 316px; }
  .card--front { left: 44px; }
  .card--back { left: 620px; }
  .card svg { display: block; width: 536px; height: 316px; }
  .fill-navy { fill: var(--navy); }
  .fill-orange { fill: var(--orange); }
  .fill-paper { fill: var(--paper); }
  .fill-white { fill: var(--white); }
  .stroke-white { stroke: var(--white); fill: none; stroke-width: 1.4; }
  .name-tag { font-size: 13.5px; font-weight: 400; fill: var(--white); }
  .name-role { font-size: 10.5px; fill: var(--white); }
  .contact { font-size: 13px; fill: var(--white); }
  .contact--small { font-size: 11.5px; }
  .wordmark { font-weight: 500; letter-spacing: 0.5px; }
  .wordmark--front { font-size: 22px; fill: var(--navy); }
  .wordmark--back { font-size: 36px; fill: var(--white); }
</style>
</head>
<body>
<main class="sheet">

  <section class="card card--front" aria-label="Business card front">
    <svg viewBox="0 0 536 316">
      <rect class="fill-paper" width="536" height="316"/>
      <polygon class="fill-navy" points="0,0 156,0 369,316 0,316"/>
      <polygon class="fill-orange" points="196,58 341,58 365,97 222,97"/>
      <text class="name-tag" x="220" y="78">NAME SURNAME</text>
      <text class="name-role" x="331" y="91" text-anchor="end">Role</text>

      <g class="contact-row">
        <circle class="fill-orange" cx="43" cy="139" r="12"/>
        <rect class="stroke-white" x="39.5" y="132" width="7" height="13" rx="1.5"/>
        <text class="contact" x="60" y="144">+1 555 0300 4127</text>
      </g>
      <g class="contact-row">
        <circle class="fill-orange" cx="43" cy="171" r="12"/>
        <path class="stroke-white" d="M36 174 q7 -9 14 0 v3 h-14 z"/>
        <text class="contact" x="60" y="176">+1 555 0148 9062</text>
      </g>
      <g class="contact-row">
        <circle class="fill-orange" cx="43" cy="204" r="12"/>
        <rect class="stroke-white" x="36" y="199" width="14" height="10"/>
        <path class="stroke-white" d="M36 199 l7 5 l7 -5"/>
        <text class="contact contact--small" x="60" y="208">info@ledgerwise.com</text>
      </g>
      <g class="contact-row">
        <circle class="fill-orange" cx="43" cy="236" r="12"/>
        <circle class="stroke-white" cx="43" cy="236" r="7"/>
        <path class="stroke-white" d="M36 236 h14 M43 229 v14"/>
        <text class="contact contact--small" x="60" y="241">www.ledgerwise.com</text>
      </g>
      <g class="contact-row">
        <circle class="fill-orange" cx="43" cy="269" r="12"/>
        <path class="fill-white" d="M43 277 l-5 -8 a5.5 5.5 0 1 1 10 0 z"/>
        <circle class="fill-orange" cx="43" cy="266" r="2"/>
        <text class="contact contact--small" x="60" y="267">Street # 6, Road Lorem Ipsum</text>
        <text class="contact contact--small" x="60" y="280">City, Region, Country. Postal Code</text>
      </g>

      <g class="logo">
        <circle class="fill-orange" cx="364" cy="247" r="6"/>
        <text class="wordmark wordmark--front" x="376" y="255">LEDGERWISE</text>
      </g>
    </svg>
  </section>

  <section class="card card--back" aria-label="Business card back">
    <svg viewBox="0 0 536 316">
      <rect class="fill-navy" width="536" height="316"/>
      <polygon class="fill-orange" points="387,0 536,0 536,316 174,316"/>
      <g class="logo">
        <circle class="fill-white" cx="157" cy="158" r="9"/>
        <text class="wordmark wordmark--back" x="176" y="171">LEDGERWISE</text>
      </g>
    </svg>
  </section>

</main>
</body>
</html>
```